Marlowe Holdings LLC - Business Cards

Need the following information on the cards:

Name: Dean R Vossler
Title: Chief Executive Manager

Business address:
412 N Ridgeview Lane #118
Linden Bluff, Il 60412

Phone: (630) 555-0148 - Business
KPV FFL license number: 5-21-xxx-xx-xx-04519
Email: dean.vossler@marloweholdingsffl.com

Target Market(s)

Firearm owners

Industry/Entity Type

Firearms industry,

Contact Information for Business Card

Contact number, name and title, web page address, email, business address and kpv license number,

Requirements
Must have
• Name, title, business address, phone numbers, KPV license numbers, web page address and email address.
Nice to have
• Cellphone number,

```html
<!DOCTYPE html>
<html lang="en">
<head>
<meta charset="utf-8">
<title>Marlowe Holdings LLC – Business Cards</title>
<link rel="stylesheet" href="https://fonts.googleapis.com/css2?family=Open+Sans:wght@300;400;600&family=Poppins:wght@600&display=swap">
<style>
  :root {
    --brand-red: #cc1a21;
    --band-gray: #bcbdbf;
    --ink: #111111;
    --paper: #ffffff;
    --backdrop: #e4e5e6;
  }
  * { margin: 0; padding: 0; box-sizing: border-box; }
  html, body { width: 1200px; height: 1000px; overflow: hidden; }
  body {
    background: var(--backdrop);
    font-family: "Open Sans", Arial, sans-serif;
    color: var(--ink);
    position: relative;
  }
  .card {
    position: absolute;
    left: 300px;
    width: 600px;
    height: 342px;
    background: var(--paper);
    box-shadow: 0 6px 18px rgba(0,0,0,0.28);
    overflow: hidden;
  }
  .card--front { top: 110px; }
  .card--back { top: 548px; }
  .card-shapes { position: absolute; inset: 0; width: 100%; height: 100%; }
  .brand-mark {
    position: absolute;
    display: flex;
    align-items: center;
    gap: 10px;
    font-family: "Poppins", Arial, sans-serif;
    font-weight: 600;
    color: var(--brand-red);
    line-height: 1.1;
  }
  .brand-mark__dot {
    flex: none;
    border-radius: 50%;
    background: var(--brand-red);
  }
  .card--front .brand-mark { left: 170px; top: 156px; font-size: 25px; }
  .card--front .brand-mark__dot { width: 22px; height: 22px; }
  .card--back .brand-mark { left: 34px; top: 156px; width: 170px; font-size: 19px; }
  .card--back .brand-mark__dot { width: 16px; height: 16px; }
  .holder {
    position: absolute;
    right: 46px;
    top: 78px;
    text-align: right;
  }
  .holder__name {
    font-family: "Poppins", Arial, sans-serif;
    font-weight: 600;
    font-size: 31px;
    line-height: 1.05;
    letter-spacing: -0.2px;
  }
  .holder__title {
    font-size: 12.5px;
    color: var(--brand-red);
    margin-top: 2px;
  }
  .contact-list {
    position: absolute;
    right: 48px;
    top: 150px;
    list-style: none;
    text-align: right;
    font-weight: 300;
    font-size: 14.5px;
    line-height: 18px;
  }
  .contact-list li {
    display: flex;
    justify-content: flex-end;
    align-items: flex-start;
    gap: 14px;
    margin-bottom: 19px;
  }
  .contact-list svg { flex: none; width: 18px; height: 18px; fill: var(--ink); margin-top: 1px; }
  .license {
    position: absolute;
    left: 0; right: 0;
    top: 293px;
    text-align: center;
    color: var(--paper);
    font-size: 15px;
    line-height: 18px;
  }
</style>
</head>
<body>

<section class="card card--front" aria-label="Business card front">
  <svg class="card-shapes" viewBox="0 0 1000 570" preserveAspectRatio="none" aria-hidden="true">
    <polygon fill="var(--brand-red)" points="0,0 1000,0 1000,6 222,167 0,52"/>
    <polygon fill="var(--band-gray)" points="0,0 905,0 225,142 0,33"/>
    <polygon fill="var(--paper)" points="0,0 885,0 225,134 0,25"/>
    <polygon fill="var(--brand-red)" points="0,0 862,0 225,128 0,18"/>
    <polygon fill="var(--brand-red)" points="785,52 1000,5 1000,178"/>
    <rect fill="var(--brand-red)" x="130" y="541" width="870" height="29"/>
    <polygon fill="var(--paper)" points="0,398 0,570 172,570"/>
    <polygon fill="var(--brand-red)" points="0,410 0,570 152,570"/>
  </svg>
  <div class="brand-mark"><span class="brand-mark__dot"></span><span>Marlowe Holdings LLC</span></div>
</section>

<section class="card card--back" aria-label="Business card back">
  <svg class="card-shapes" viewBox="0 0 1000 570" preserveAspectRatio="none" aria-hidden="true">
    <polygon fill="var(--brand-red)" points="0,0 1000,0 1000,6 222,167 0,52"/>
    <polygon fill="var(--band-gray)" points="0,0 905,0 225,142 0,33"/>
    <polygon fill="var(--paper)" points="0,0 885,0 225,134 0,25"/>
    <polygon fill="var(--brand-red)" points="0,0 862,0 225,128 0,18"/>
    <polygon fill="var(--brand-red)" points="785,52 1000,5 1000,178"/>
    <rect fill="var(--band-gray)" x="0" y="462" width="1000" height="12"/>
    <rect fill="var(--brand-red)" x="0" y="474" width="1000" height="96"/>
  </svg>

  <div class="brand-mark"><span class="brand-mark__dot"></span><span>Marlowe Holdings LLC</span></div>

  <div class="holder">
    <div class="holder__name">Dean R Vossler</div>
    <div class="holder__title">CHIEF EXECUTIVE MANAGER</div>
  </div>

  <ul class="contact-list">
    <li><span>(630) 555-0148</span>
      <svg viewBox="0 0 24 24" aria-hidden="true"><path d="M2 9c0-3 5-5 10-5s10 2 10 5v2h-5V9c-1-1-3-1.5-5-1.5S8 8 7 9v2H2z"/><path d="M6 12l2-3h8l2 3v8H6z"/><circle cx="12" cy="15.5" r="2.2" fill="#fff"/></svg>
    </li>
    <li><span>dean.vossler@marloweholdingsffl.com</span>
      <svg viewBox="0 0 24 24" aria-hidden="true"><path d="M2 5h20v14H2z"/><path d="M3 6l9 7 9-7M3 18l7-6M21 18l-7-6" stroke="#fff" stroke-width="1.6" fill="none"/></svg>
    </li>
    <li><span>412 N Ridgeview Lane #118<br>Linden Bluff, Il 60412</span>
      <svg viewBox="0 0 24 24" aria-hidden="true"><path d="M12 1a7 7 0 0 0-7 7c0 5 7 12 7 12s7-7 7-12a7 7 0 0 0-7-7zm0 10a3 3 0 1 1 0-6 3 3 0 0 1 0 6z"/><ellipse cx="12" cy="22" rx="5" ry="1.3"/></svg>
    </li>
  </ul>

  <p class="license">KPV FFL license number<br>5-21-xxx-xx-xx-04519</p>
</section>

</body>
</html>
```